Craft Beer Needs a Label/ Logo Design

Name: Lanternfall
(Lanternfall Ale, Lanternfall Pilsner, Lanternfall Stout)

We are looking for a logo-ed label that will resonate domestically and internationally for this new Craft Beer Brand.

Target Market(s)

Millenials

Logo Text

Lanternfall Pilsner

Logo styles of interest
Emblem Logo
Character Logo
Colors

Designer to choose colors to be used in the design.

Requirements
Must have
• A labled logo design -- "Lanternfall" is the name, but would like to see samples with "Ale", "Pilsner", or "Stout" after!

```html
<!DOCTYPE html>
<html lang="en">
<head>
<meta charset="utf-8">
<title>Lanternfall Pilsner – Craft Beer Label</title>
<link href="https://fonts.googleapis.com/css2?family=Libre+Caslon+Text&display=swap" rel="stylesheet">
<style>
  :root {
    --page: #ffffff;
    --ink: #221c19;
    --cream: #e4dbbd;
    --ray: #4b4746;
    --gold-light: #fbf3dc;
    --gold: #d6a33a;
    --bronze: #a8682a;
    --oxblood: #6e2e26;
    --stripe-light: #cfc6ad;
    --stripe-dark: #5a524a;
  }
  html, body {
    margin: 0;
    padding: 0;
    width: 959px;
    height: 1200px;
    overflow: hidden;
    background: var(--page);
  }
  .label {
    display: block;
    width: 959px;
    height: 1200px;
  }
  .label-ink { fill: var(--ink); }
  .label-cream { fill: var(--cream); }
  .brand-mark { fill: var(--gold); }
  .brand-name {
    font-family: "Libre Caslon Text", serif;
    font-size: 104px;
    fill: var(--cream);
  }
  .tagline {
    font-family: "Libre Caslon Text", serif;
    font-size: 40px;
    fill: var(--cream);
  }
  .beer-style {
    font-family: "Libre Caslon Text", serif;
    font-size: 62px;
    fill: var(--cream);
  }
  .origin {
    font-family: "Libre Caslon Text", serif;
    font-size: 27px;
    fill: var(--cream);
    letter-spacing: 1px;
  }
</style>
</head>
<body>
<svg class="label" viewBox="0 0 959 1200" xmlns="http://www.w3.org/2000/svg" aria-labelledby="label-title">
  <title id="label-title">Lanternfall Pilsner craft beer label</title>
  <defs>
    <linearGradient id="rim-metal" x1="0" y1="0" x2="1" y2="0">
      <stop offset="0" stop-color="var(--gold)"/>
      <stop offset="0.12" stop-color="var(--gold-light)"/>
      <stop offset="0.35" stop-color="var(--gold)"/>
      <stop offset="0.7" stop-color="var(--bronze)"/>
      <stop offset="1" stop-color="var(--oxblood)"/>
    </linearGradient>
    <linearGradient id="inner-rim-metal" x1="0" y1="0" x2="1" y2="1">
      <stop offset="0" stop-color="var(--gold)"/>
      <stop offset="0.4" stop-color="var(--gold-light)"/>
      <stop offset="0.7" stop-color="var(--gold)"/>
      <stop offset="1" stop-color="var(--bronze)"/>
    </linearGradient>
    <linearGradient id="ring-tone" x1="0" y1="0" x2="1" y2="1">
      <stop offset="0" stop-color="var(--stripe-light)"/>
      <stop offset="1" stop-color="var(--stripe-dark)"/>
    </linearGradient>
    <linearGradient id="ray-tone" x1="0" y1="0" x2="0" y2="1">
      <stop offset="0" stop-color="var(--ray)"/>
      <stop offset="1" stop-color="#3a3634"/>
    </linearGradient>
    <clipPath id="label-face">
      <ellipse cx="490" cy="625" rx="370" ry="458"/>
    </clipPath>
    <clipPath id="center-panel">
      <ellipse cx="492" cy="620" rx="290" ry="362"/>
    </clipPath>
  </defs>

  <ellipse class="outer-rim" cx="490" cy="625" rx="386" ry="476" fill="url(#rim-metal)"/>

  <ellipse class="stripe-ring" cx="490" cy="625" rx="370" ry="458" fill="url(#ring-tone)"
           role="img" aria-label="Fine diagonal pinstripe pattern in cream and dark brown"/>

  <ellipse class="inner-rim" cx="492" cy="620" rx="302" ry="374" fill="url(#inner-rim-metal)"/>
  <ellipse class="label-ink center-panel" cx="492" cy="620" rx="290" ry="362"/>

  <g clip-path="url(#center-panel)">
    <rect class="sunburst" x="190" y="250" width="610" height="140" fill="url(#ray-tone)"
          role="img" aria-label="Grey radiating rays at the top of the panel"/>
  </g>

  <circle class="brand-mark" cx="490" cy="390" r="34"/>

  <text class="tagline" x="378" y="434" text-anchor="middle">Craft</text>
  <text class="tagline" x="607" y="434" text-anchor="middle">Beer</text>

  <g class="name-band" clip-path="url(#label-face)">
    <rect class="label-cream band-edge" x="0" y="500" width="959" height="14"/>
    <rect class="label-ink band" x="0" y="514" width="959" height="204"/>
    <rect class="label-cream band-edge" x="0" y="718" width="959" height="14"/>
  </g>
  <text class="brand-name" x="490" y="652" text-anchor="middle">Lanternfall</text>

  <text class="beer-style" x="490" y="864" text-anchor="middle">Pilsner</text>
  <text class="origin" x="488" y="920" text-anchor="middle">Arizona</text>
</svg>
</body>
</html>
```